Spark of Meadow Paddocks Business Cards with logo

Need a creative business card that pops. Colorful but professional. The attached logo should be included. We are a national horse racing partnership so we are in the equine business. Nothing cartoonlike or whimsical.

Target Market(s)

professionals - 40+

Contact Information for Business Card

Dana Whitlow
Director of Operations
27 Pinecrest Lane
Brookfield, MD. 20999

Phone (555) 274-6183

FX: (555) 619-3047

email: dana@smpaddocks.example
smpaddocks.example

Requirements
Must have
• All information above should be on the business card including the website address. Professional yet creative
Nice to have
• an attention grabbing design. not boring. exciting.
Should not have
• cartoon like - whimsical.

```html
<!DOCTYPE html>
<html lang="en">
<head>
<meta charset="utf-8">
<title>Spark of Meadow Paddocks – Business Cards</title>
<link rel="stylesheet" href="https://fonts.googleapis.com/css2?family=Montserrat:wght@400;500;700&display=swap">
<style>
  :root {
    --navy: #232c6b;
    --gold: #b08a2c;
    --paper: #f4f4f4;
    --ink: #1d1d1f;
    --backdrop: #d9d9d9;
  }
  * { box-sizing: border-box; margin: 0; padding: 0; }
  html, body { width: 1200px; height: 1021px; overflow: hidden; }
  body {
    background: var(--backdrop);
    font-family: "Montserrat", sans-serif;
    position: relative;
  }
  .card {
    position: absolute;
    left: 250px;
    width: 700px;
    height: 400px;
    box-shadow: 0 8px 24px rgba(0,0,0,0.18);
  }
  .card--back { top: 70px; background: var(--navy); }
  .card--front { top: 550px; background: var(--paper); }

  .brand {
    position: absolute;
    width: 230px;
    height: 230px;
    border: 2px solid var(--gold);
    border-radius: 50%;
    display: flex;
    align-items: center;
    justify-content: center;
    text-align: center;
    padding: 30px;
    font-weight: 700;
    font-size: 22px;
    letter-spacing: 0.14em;
    line-height: 1.35;
    text-transform: uppercase;
  }
  .card--back .brand { left: 235px; top: 85px; color: #ffffff; }
  .card--front .brand { left: 60px; top: 85px; color: var(--navy); }

  .contact {
    position: absolute;
    left: 380px;
    top: 105px;
    color: var(--ink);
  }
  .contact__name { color: var(--navy); font-weight: 700; font-size: 25px; }
  .contact__title { font-size: 17px; margin-top: 2px; }
  .contact__rule { width: 44px; height: 3px; background: var(--gold); margin: 14px 0 16px; }
  .contact__address { font-size: 16px; line-height: 1.3; margin-bottom: 8px; }
  .contact__list { list-style: none; font-size: 16px; line-height: 1.45; }
  .contact__list li { display: flex; align-items: center; gap: 8px; }
  .contact__list svg { width: 15px; height: 15px; flex: none; }
</style>
</head>
<body>
  <section class="card card--back" aria-label="Card back">
    <div class="brand">Spark of Meadow Paddocks</div>
  </section>

  <section class="card card--front" aria-label="Card front">
    <div class="brand">Spark of Meadow Paddocks</div>
    <div class="contact">
      <p class="contact__name">Dana Whitlow</p>
      <p class="contact__title">Director of Operations</p>
      <div class="contact__rule"></div>
      <p class="contact__address">27 Pinecrest Lane<br>Brookfield, MD. 20999</p>
      <ul class="contact__list">
        <li>
          <svg viewBox="0 0 16 16" aria-hidden="true"><path fill="#b08a2c" d="M3 1l3 3-1.5 2a9 9 0 005.5 5.5L12 10l3 3-2 2C7 15 1 9 1 3z"/></svg>
          (555) 274-6183
        </li>
        <li>
          <svg viewBox="0 0 16 16" aria-hidden="true"><path fill="#b08a2c" d="M4 1h8v4H4zM1 6h14v7h-3v2H4v-2H1zM5 10v4h6v-4z"/></svg>
          (555) 619-3047
        </li>
        <li>
          <svg viewBox="0 0 16 16" aria-hidden="true"><rect x="1" y="3" width="14" height="10" fill="none" stroke="#b08a2c" stroke-width="1.6"/><path d="M1 3l7 6 7-6" fill="none" stroke="#b08a2c" stroke-width="1.6"/></svg>
          dana@smpaddocks.example
        </li>
        <li>
          <svg viewBox="0 0 16 16" aria-hidden="true"><circle cx="8" cy="8" r="6.5" fill="none" stroke="#b08a2c" stroke-width="1.5"/><ellipse cx="8" cy="8" rx="3" ry="6.5" fill="none" stroke="#b08a2c" stroke-width="1.2"/><path d="M1.5 8h13" stroke="#b08a2c" stroke-width="1.2"/></svg>
          smpaddocks.example
        </li>
      </ul>
    </div>
  </section>
</body>
</html>
```